Womans Supplement Designs

Launching a Supplement company and need to get some initial designs created, I've attached our logo and the bottle type that I want the samples done one.

This project is for our Whey Protein we are starting with Vanilla, chocolate and strawberry banana

(ALL DESIGN VARIATIONS MUST BE A WHITE BOTTLE NOT BLACK)

(FOR DESIGN SAMPLES PLEASE USE THE SUPPLEMENT BOTTLE STYLE I PROVIDED)

Whoever is selected the winner I will have more work for you to complete the disigns for the rest of the products in the line, Just want to get this shake completed first

Target Market(s)

Women

Requirements
Must have
• Must have our current logo involved

the name of this product will be "KIVA LUM"

Must have this slogan,

ALL-IN-ONE PREMIUM PROTEIN NUTRITIONAL SHAKE FOR BLACK WOMEN

This is our meal replacement

the design should try to keep the same look and feel of the existing provided supplement images

we are starting with chocolate, vanilla and strawberry banana

this is for women and should look colorful and appeal to them
Should not have
• Do not use an image of a person or lady, don't want it branded to a person

```html
<!DOCTYPE html>
<html lang="en">
<head>
<meta charset="utf-8">
<title>KIVA LUM – Protein Shake Label</title>
<link rel="stylesheet" href="https://fonts.googleapis.com/css2?family=Exo+2:ital,wght@0,600;0,800;1,900&family=Oswald:wght@300&family=Russo+One&display=swap">
<style>
  :root {
    --purple-deep: #561586;
    --purple: #7a24ad;
    --purple-ink: #4e1670;
    --gold: #e9b22c;
    --gold-dark: #d39a1c;
    --white: #ffffff;
    --label-white: #f3f3f5;
    --ink: #111111;
    --cocoa: #7a4526;
    --cocoa-dark: #4c2814;
    --grey-text: #333333;
  }
  html, body {
    margin: 0;
    padding: 0;
    width: 1200px;
    height: 1034px;
    overflow: hidden;
    background: var(--white);
  }
  .canvas {
    position: relative;
    width: 1200px;
    height: 1034px;
  }
  .brand-header {
    position: absolute;
    top: 150px;
    left: 0;
    width: 1200px;
    display: flex;
    justify-content: center;
    align-items: center;
    gap: 22px;
  }
  .brand-dot {
    width: 34px;
    height: 34px;
    border-radius: 50%;
    background: var(--ink);
  }
  .brand-name {
    font-family: "Exo 2", sans-serif;
    font-weight: 600;
    font-size: 58px;
    letter-spacing: 8px;
    color: var(--ink);
  }
  .label {
    position: absolute;
    left: 150px;
    top: 310px;
    width: 900px;
    height: 680px;
  }
  .label-brand { font-family: "Exo 2", sans-serif; font-weight: 600; font-size: 30px; letter-spacing: 5px; fill: var(--white); }
  .product-name { font-family: "Exo 2", sans-serif; font-weight: 900; font-style: italic; font-size: 118px; fill: var(--ink); letter-spacing: 2px; }
  .slogan { font-family: "Exo 2", sans-serif; font-weight: 800; font-size: 27px; fill: var(--purple-ink); }
  .flavour { font-family: "Russo One", sans-serif; font-style: italic; font-size: 32px; fill: var(--label-white); letter-spacing: 1px; }
  .net-weight { font-family: "Oswald", sans-serif; font-weight: 300; font-size: 24px; fill: var(--grey-text); letter-spacing: 1px; }
  .serving-count { font-family: "Russo One", sans-serif; font-size: 62px; fill: var(--gold); }
  .serving-word { font-family: "Russo One", sans-serif; font-size: 20px; fill: var(--white); letter-spacing: 1px; }
  .natural-note { font-family: "Exo 2", sans-serif; font-weight: 800; font-size: 14px; fill: var(--purple-ink); }
  .category { font-family: "Russo One", sans-serif; font-size: 26px; fill: var(--white); letter-spacing: 2px; }
</style>
</head>
<body>
<main class="canvas">
  <header class="brand-header">
    <span class="brand-dot"></span>
    <span class="brand-name">NOVA HAVEN</span>
  </header>

  <svg class="label" viewBox="0 0 900 680" xmlns="http://www.w3.org/2000/svg">
    <defs>
      <linearGradient id="purpleField" x1="0" y1="0" x2="1" y2="0">
        <stop offset="0" stop-color="var(--purple-deep)"/>
        <stop offset="0.5" stop-color="var(--purple)"/>
        <stop offset="1" stop-color="var(--purple-deep)"/>
      </linearGradient>
      <linearGradient id="goldBand" x1="0" y1="0" x2="1" y2="0">
        <stop offset="0" stop-color="var(--gold)"/>
        <stop offset="0.5" stop-color="var(--gold-dark)"/>
        <stop offset="1" stop-color="var(--gold)"/>
      </linearGradient>
      <linearGradient id="cocoaPill" x1="0" y1="0" x2="1" y2="0">
        <stop offset="0" stop-color="var(--cocoa)"/>
        <stop offset="1" stop-color="var(--cocoa-dark)"/>
      </linearGradient>
      <radialGradient id="cocoaSplash" cx="0.5" cy="0.5" r="0.5">
        <stop offset="0" stop-color="#8a5433"/>
        <stop offset="1" stop-color="#3f2010"/>
      </radialGradient>
    </defs>

    <rect class="label-field" x="0" y="0" width="900" height="680" fill="url(#purpleField)"/>

    <text class="label-brand" x="450" y="120" text-anchor="middle">NOVA HAVEN</text>

    <path class="gold-band" d="M150 200 H750 Q770 200 780 215 L900 395 V640 H0 V395 L120 215 Q130 200 150 200 Z" fill="url(#goldBand)"/>
    <text class="product-name" x="450" y="320" text-anchor="middle">KIVA LUM</text>

    <path class="white-panel" d="M205 335 H695 Q712 335 722 350 L900 575 V640 H0 V575 L178 350 Q188 335 205 335 Z" fill="var(--label-white)"/>

    <text class="slogan" x="450" y="385" text-anchor="middle">ALL-IN-ONE PREMIUM</text>
    <text class="slogan" x="450" y="417" text-anchor="middle">PROTEIN NUTRITIONAL SHAKE</text>
    <text class="slogan" x="450" y="449" text-anchor="middle">FOR BLACK WOMEN</text>

    <rect class="flavour-pill" x="230" y="475" width="410" height="48" rx="24" fill="url(#cocoaPill)"/>
    <text class="flavour" x="435" y="511" text-anchor="middle">CHOCOLATE</text>

    <ellipse class="flavour-visual" role="img" aria-label="Chocolate pieces in a splash of melted chocolate" cx="660" cy="495" rx="78" ry="68" fill="url(#cocoaSplash)"/>

    <text class="net-weight" x="450" y="562" text-anchor="middle">30 SERVING .NET 250G</text>

    <g class="diet-badges" fill="none" stroke="var(--gold-dark)" stroke-width="3">
      <circle cx="370" cy="605" r="27"/>
      <circle cx="445" cy="605" r="27"/>
      <circle cx="520" cy="605" r="27"/>
    </g>

    <rect class="category-strip" x="0" y="640" width="900" height="40" fill="var(--purple-ink)"/>
    <text class="category" x="470" y="670" text-anchor="middle">PROTEIN SUPPLEMENT</text>

    <g class="serving-tag">
      <path d="M50 565 Q50 545 70 545 H190 Q210 545 210 565 V680 H50 Z" fill="var(--purple-deep)"/>
      <path d="M50 625 H210 V668 Q210 680 198 680 H62 Q50 680 50 668 Z" fill="var(--gold)"/>
      <text class="serving-count" x="130" y="598" text-anchor="middle">30</text>
      <text class="serving-word" x="130" y="620" text-anchor="middle">SERVING</text>
      <text class="natural-note" x="130" y="648" text-anchor="middle">ALL NATURAL</text>
      <text class="natural-note" x="130" y="666" text-anchor="middle">PLANT BASED</text>
    </g>
  </svg>
</main>
</body>
</html>
```